Flyer Design Project

Family owned and operated roof repair, cleaning and restoration business. Offering quality service and product at a quality price. Have been in existence for over 25 years.
I have just had a logo designed for the business. I would like to generate business by getting people to look at their roof and consider the maintenance and appearance.
Must generate a serious approach as there have been some operators who have acted poorly.
We DO NOT pressure sell, but gladly provide quotes and advice. We only use the best quality products and we are a licensed applicator of this product.
Our finished product will protect homes and increase their value.
Target Market(s)
Home owners who have a house with concrete roof tiles.
Industry/Entity Type
Business
Look and feel

```html
<!DOCTYPE html>
<html lang="en">
<head>
<meta charset="utf-8">
<title>TRU-GUARD Roof Restoration Flyer</title>
<link href="https://fonts.googleapis.com/css2?family=Cinzel:wght@600;700&family=Open+Sans:ital,wght@0,600;0,700;1,600;1,700;1,800&family=Ubuntu:wght@400;500&display=swap" rel="stylesheet">
<style>
  :root {
    --ink: #1d1d1f;
    --white: #ffffff;
    --paper: #f7f7f7;
    --grey: #8a8a8a;
    --grey-dark: #4a4a4a;
    --blue: #2f8fd6;
    --blue-light: #5ab4f0;
    --black: #050505;
    --sky-top: #dfe9f3;
    --sky-low: #b9cde2;
    --roof: #6b5038;
    --roof-dark: #4a3626;
    --brick: #d9c6a4;
    --lawn: #4f6b2e;
  }
  * { margin: 0; padding: 0; box-sizing: border-box; }
  html, body { width: 1200px; height: 2544px; overflow: hidden; background: var(--paper); }
  .flyer {
    position: relative; width: 1200px; height: 2544px; overflow: hidden;
    background: var(--white); font-family: "Open Sans", sans-serif; color: var(--ink);
  }
  .hero-photo {
    position: absolute; left: 36px; top: 28px; width: 1128px; height: 1172px;
    background: linear-gradient(180deg, var(--sky-top) 0%, var(--sky-low) 16%, var(--roof) 30%, var(--roof-dark) 48%, var(--brick) 62%, var(--brick) 74%, var(--lawn) 86%, #2d3a1c 100%);
  }
  .hero-photo::after {
    content: ""; position: absolute; left: 0; right: 0; bottom: 0; height: 300px;
    background: linear-gradient(180deg, rgba(0,0,0,0) 0%, rgba(0,0,0,0.55) 100%);
  }
  .headline {
    position: absolute; left: 0; top: 30px; width: 1200px; text-align: center;
    font-family: "Cinzel", serif; color: var(--black); line-height: 1;
  }
  .headline-small { display: block; font-size: 78px; font-weight: 700; letter-spacing: 2px; }
  .headline-large { display: block; font-size: 120px; font-weight: 700; margin-top: 4px; letter-spacing: 1px; }
  .tagline {
    position: absolute; right: 70px; top: 1020px; text-align: right; white-space: nowrap;
    font-style: italic; font-weight: 700; font-size: 66px; line-height: 1.1; color: var(--white);
    text-shadow: 0 3px 8px rgba(0,0,0,0.6);
  }
  .tagline .accent { color: var(--blue-light); }
  .credentials {
    position: absolute; left: 48px; top: 1234px; white-space: nowrap;
    font-style: italic; font-weight: 700; font-size: 58px; line-height: 1.15; color: var(--grey);
  }
  .credentials .strong { color: var(--grey-dark); }
  .brand-panel {
    position: absolute; left: 48px; top: 1408px; width: 1104px; height: 580px;
    background: var(--black); border: 12px solid var(--blue);
    display: flex; align-items: center; justify-content: center; gap: 40px;
  }
  .brand-mark { width: 70px; height: 70px; background: var(--blue); flex: none; }
  .brand-name {
    font-family: "Open Sans", sans-serif; font-weight: 700; color: var(--white);
    font-size: 130px; line-height: 1; white-space: nowrap;
  }
  .brand-name span { display: block; font-size: 74px; margin-top: 16px; }
  .heritage {
    position: absolute; left: 0; width: 1200px; top: 2026px; text-align: center;
    white-space: nowrap; line-height: 1.2;
    font-style: italic; font-weight: 700; font-size: 46px; color: var(--grey-dark);
  }
  .quotes {
    position: absolute; left: 0; width: 1200px; top: 2128px; text-align: center;
    font-family: "Ubuntu", sans-serif; color: var(--black);
  }
  .quotes-title {
    display: inline-block; font-size: 92px; font-weight: 400; line-height: 1;
    border-bottom: 10px solid var(--blue); padding: 0 10px 6px;
  }
  .quotes-sub { display: block; font-size: 50px; line-height: 1.2; margin-top: 6px; }
  .call-bar {
    position: absolute; left: 0; bottom: 0; width: 1200px; height: 180px;
    background: linear-gradient(180deg, #3a3a3a 0%, var(--black) 60%);
    display: flex; align-items: center; justify-content: center; gap: 36px;
    color: var(--white); font-style: italic; font-weight: 700; white-space: nowrap;
  }
  .call-label { font-size: 66px; }
  .call-number { font-size: 104px; letter-spacing: 2px; }
</style>
</head>
<body>
<main class="flyer">
  <div class="hero-photo" role="img" aria-label="Photo of a brick family home with a brown tiled roof, white garage door and front garden"></div>
  <h1 class="headline">
    <span class="headline-small">Attention</span>
    <span class="headline-large">HOME OWNERS</span>
  </h1>
  <p class="tagline">Protect <span class="accent">your</span> roofs<br><span class="accent">now as how they</span> protect you...</p>
  <p class="credentials">Licenced applicator <span class="strong">with best in<br>quality, product &amp; price</span></p>
  <section class="brand-panel">
    <div class="brand-mark"></div>
    <div class="brand-name">TRU-GUARD<span>Roof Restoration</span></div>
  </section>
  <p class="heritage">A family owned Roofing Solutions over 25 years</p>
  <div class="quotes">
    <span class="quotes-title">Quotes &amp; Guide</span>
    <span class="quotes-sub">Solutions at your door step</span>
  </div>
  <footer class="call-bar">
    <span class="call-label">CALL US TODAY</span>
    <span class="call-number">0198765432</span>
  </footer>
</main>
</body>
</html>
```